KTR Engineering Pty Ltd

I have already had Corvale welding and fabrication cards made , my business has changed too KTR engineering Pty Ltd so I need my logo changed on the cards
one side have my logo then the other side have what we do.
front side logo and details
owner /operator : Lachlan Meravic
email: ktr.works@ironvalemail.com
number: 0491537204
ABN: 47 261 538 902
ACN: 718 352 946
on back have in dot points what we do:
* structural steel erection
* precast panels
* site welding
*steel alteration & repair
* rigging & dogging
*labour hire
all details in breif

```html
<!DOCTYPE html>
<html lang="en">
<head>
<meta charset="utf-8">
<title>KTR Engineering Pty Ltd — Business Cards</title>
<link rel="stylesheet" href="https://fonts.googleapis.com/css2?family=Open+Sans:wght@400;600;700;800&display=swap">
<style>
  :root {
    --backdrop: #dcdddf;
    --card-white: #f2f1ef;
    --navy: #0f1b2b;
    --rust: #a8392c;
    --grey: #6d6e70;
    --white: #ffffff;
  }
  * { box-sizing: border-box; margin: 0; padding: 0; }
  html, body {
    width: 1200px; height: 1051px; overflow: hidden;
    background: var(--backdrop);
    font-family: "Open Sans", Arial, sans-serif;
  }
  .card-set {
    position: relative; width: 1200px; height: 1051px;
  }
  .card {
    position: absolute; width: 520px; height: 297px;
    border-radius: 3px;
    box-shadow: 0 12px 28px rgba(0,0,0,0.18);
  }
  .card--front { left: 60px; top: 420px; background: var(--card-white); }
  .card--back { left: 620px; top: 334px; background: var(--navy); }

  .brand { position: absolute; }
  .brand__row { display: flex; align-items: center; gap: 10px; }
  .brand__dot { width: 14px; height: 14px; border-radius: 50%; background: var(--rust); flex: none; }
  .brand__name {
    font-weight: 800; font-size: 23px; line-height: 1.15;
    letter-spacing: 0.5px; text-transform: uppercase;
  }
  .brand__phone {
    margin-top: 6px; margin-left: 24px;
    font-size: 12px; font-weight: 600; letter-spacing: 2px; color: var(--rust);
  }

  .card--front .brand { left: 30px; top: 78px; width: 230px; }
  .card--front .brand__name { color: var(--navy); }

  .divider {
    position: absolute; left: 272px; top: 78px;
    width: 1.5px; height: 130px; background: var(--navy);
  }
  .contact { position: absolute; left: 292px; top: 84px; }
  .contact__name { font-size: 20px; font-weight: 700; color: var(--navy); }
  .contact__role { font-size: 14px; color: var(--rust); margin-top: 1px; }
  .contact__line {
    display: flex; align-items: center; gap: 7px;
    font-size: 13px; color: var(--grey); margin-top: 6px;
  }
  .contact__role + .contact__line { margin-top: 14px; }
  .contact__line svg { width: 12px; height: 12px; fill: var(--rust); flex: none; }

  .registration {
    position: absolute; left: 30px; bottom: 30px;
    font-size: 13px; color: var(--grey); letter-spacing: 0.3px;
  }
  .sep { color: var(--rust); margin: 0 8px; }

  .card--back .brand { left: 0; right: 0; top: 78px; display: flex; flex-direction: column; align-items: center; }
  .card--back .brand__name { color: var(--white); font-size: 26px; }
  .card--back .brand__phone { margin-left: 24px; }

  .services {
    position: absolute; left: 40px; right: 40px; bottom: 44px;
    list-style: none; color: var(--white); font-size: 14px; line-height: 1.55;
    text-align: center;
  }
</style>
</head>
<body>
<main class="card-set">

  <section class="card card--front" aria-label="Front of card">
    <div class="brand">
      <div class="brand__row">
        <span class="brand__dot"></span>
        <span class="brand__name">KTR Engineering Pty Ltd</span>
      </div>
      <div class="brand__phone">0491537204</div>
    </div>

    <div class="divider"></div>

    <div class="contact">
      <div class="contact__name">Lachlan Meravic</div>
      <div class="contact__role">owner / operator</div>
      <div class="contact__line">
        <svg viewBox="0 0 24 24" aria-hidden="true"><path d="M6.6 10.8a15.1 15.1 0 0 0 6.6 6.6l2.2-2.2a1 1 0 0 1 1-.25 11.4 11.4 0 0 0 3.6.57 1 1 0 0 1 1 1V20a1 1 0 0 1-1 1A17 17 0 0 1 3 4a1 1 0 0 1 1-1h3.5a1 1 0 0 1 1 1c0 1.25.2 2.45.57 3.57a1 1 0 0 1-.25 1z"/></svg>
        <span>0491537204</span>
      </div>
      <div class="contact__line">
        <svg viewBox="0 0 24 24" aria-hidden="true"><path d="M2 5h20v2l-10 6L2 7zm0 4.3l10 6 10-6V19H2z"/></svg>
        <span>ktr.works@ironvalemail.com</span>
      </div>
    </div>

    <div class="registration">ABN: 47 261 538 902<span class="sep">•</span>ACN: 718 352 946</div>
  </section>

  <section class="card card--back" aria-label="Back of card">
    <div class="brand">
      <div class="brand__row">
        <span class="brand__dot"></span>
        <span class="brand__name">KTR Engineering Pty Ltd</span>
      </div>
      <div class="brand__phone">0491537204</div>
    </div>

    <ul class="services">
      <li>structural steel erection<span class="sep">•</span>precast panels<span class="sep">•</span>site welding</li>
      <li>steel alteration &amp; repair<span class="sep">•</span>rigging &amp; dogging<span class="sep">•</span>labour hire</li>
    </ul>
  </section>

</main>
</body>
</html>
```